Product Catalogue for Brand New Range in Growing Small Business

We require a product catalogue for a new range (bollards and barriers) to be supplied to industrial and commercial customers within New Zealand. There will be about three variations to display of one product, one-two images of each product. We already supply FRP, steel, and safety products nationwide. We have the required files and text copy, including branding guidelines to follow. Clean, professional style designed to clearly communicate and showcase new products to customers. I have supplied images showing examples of what the products look like, some inspiration and what current branding looks like. Black, white, grey.

Target Market(s)

Industrial, Commercial, Warehouse

Industry/Entity Type

Industrial, Commercial, Warehouse Environments

Font styles to use
Other font styles liked:
• Poppins

Colors

Designer to choose colors to be used in the design.

Requirements
Must have
• Our supplied copy and images, company branding applied

```html
<!DOCTYPE html>
<html lang="en">
<head>
<meta charset="UTF-8">
<title>Bollards &amp; Barriers Catalogue 2025</title>
<link href="https://fonts.googleapis.com/css2?family=Archivo:wdth,wght@125,900&family=Poppins:ital,wght@0,400;0,500;0,600;0,700;1,600&display=swap" rel="stylesheet">
<style>
  :root {
    --ink: #0f0f0f;
    --yellow: #f5dc63;
    --white: #ffffff;
    --text: #1c1c1c;
    --logo-grey: #8a8a8a;
    --brand-grey: #b9b9b9;
  }
  * { margin: 0; padding: 0; box-sizing: border-box; }
  html, body { width: 1200px; height: 1200px; overflow: hidden; background: var(--white); }
  body { position: relative; font-family: "Poppins", sans-serif; color: var(--text); }
  .abs { position: absolute; }

  .page { position: absolute; width: 473px; height: 473px; overflow: hidden; }
  .black { background: var(--ink); }
  .yellow { background: var(--yellow); }
  .photo { position: absolute; }

  .brand { position: absolute; display: flex; align-items: center; gap: 8px; color: var(--brand-grey); font-size: 10px; letter-spacing: .04em; font-weight: 500; }
  .brand-square { width: 30px; height: 30px; background: var(--logo-grey); }

  /* Cover */
  .cover { left: 110px; top: 80px; background: var(--white); }
  .cover-title { font-family: "Archivo", sans-serif; font-weight: 900; font-stretch: 125%; font-variation-settings: "wdth" 125; color: var(--white); font-size: 40px; line-height: 38px; letter-spacing: .01em; }
  .cover-sub { color: var(--white); font-size: 20px; font-weight: 500; }
  .cover-tag { color: var(--white); font-size: 13px; font-weight: 500; line-height: 17px; text-transform: uppercase; }
  .cover-year { font-style: italic; font-weight: 600; font-size: 15px; color: var(--ink); }

  /* Headings */
  .heading { font-weight: 600; color: var(--ink); }
  .body-copy { font-size: 9.6px; line-height: 17px; color: var(--text); }
  .quote-copy { font-size: 9.4px; line-height: 17px; font-weight: 600; color: var(--white); }
  .quote-mark { font-family: "Archivo", sans-serif; font-weight: 900; font-size: 38px; color: var(--white); font-style: italic; line-height: 1; }
  .page-no { position: absolute; width: 29px; height: 27px; background: var(--yellow); font-size: 12px; display: flex; align-items: center; justify-content: center; color: var(--ink); }

  .spec-title { font-size: 10px; font-weight: 600; }
  .spec-list { list-style: none; font-size: 9.6px; line-height: 17px; }
  .spec-list li { position: relative; white-space: nowrap; }
  .spec-list li::before { content: ""; position: absolute; left: -14px; top: 7px; width: 4px; height: 4px; background: var(--yellow); }

  .contact-copy { font-size: 9.6px; line-height: 17px; color: var(--white); }
  .contact-list { list-style: none; font-size: 9.6px; color: var(--white); }
  .contact-list li { display: flex; align-items: center; gap: 10px; height: 20px; white-space: nowrap; }
  .contact-list svg { width: 13px; height: 13px; flex: none; }
</style>
</head>
<body>

<!-- Cover -->
<section class="page cover">
  <div class="abs black" style="left:0;top:0;width:261px;height:465px;"></div>
  <div class="photo" role="img" aria-label="Stainless steel bollards with yellow bands lining a warehouse forecourt with trucks" style="left:261px;top:0;width:212px;height:420px;background:linear-gradient(180deg,#cfdbe2 0%,#9aa5ab 35%,#c9ccc9 60%,#e3e3de 100%);"></div>
  <div class="abs yellow" style="left:261px;top:420px;width:212px;height:53px;"></div>
  <div class="abs yellow" style="left:0;top:465px;width:261px;height:8px;"></div>
  <div class="brand" style="left:35px;top:33px;"><span class="brand-square"></span>ARDEN LIMITED</div>
  <div class="abs cover-title" style="left:35px;top:147px;">NEW<br>RANGE</div>
  <div class="abs cover-sub" style="left:35px;top:228px;">IS HERE!</div>
  <div class="abs cover-tag" style="left:35px;top:294px;">Bollards &amp; Barriers<br>for safer industrial<br>environments</div>
  <div class="abs cover-year" style="left:309px;top:436px;">Catalogue 2025</div>
</section>

<!-- Welcome -->
<section class="page" style="left:622px;top:78px;">
  <div class="abs black" style="left:249px;top:0;width:224px;height:473px;"></div>
  <div class="abs yellow" style="left:0;top:43px;width:348px;height:82px;"></div>
  <div class="abs yellow" style="left:0;top:125px;width:9px;height:348px;"></div>
  <div class="abs heading" style="left:61px;top:55px;font-size:27.5px;line-height:29px;">Welcome<br>To Our New Range</div>
  <p class="abs body-copy" style="left:45px;top:161px;width:174px;">We are proud to introduce our latest range of bollards and barriers, designed for maximum durability, safety, and functionality. With a strong presence in the FRP, steel, and safety product sectors, we now expand our portfolio to include versatile solutions for industrial and commercial customers nationwide. This catalogue presents the latest designs tailored to meet the evolving needs of New Zealand businesses.</p>
  <div class="abs quote-mark" style="left:273px;top:163px;">“</div>
  <p class="abs quote-copy" style="left:294px;top:192px;width:144px;">Our bollards and barriers are engineered to withstand harsh environments, ensuring long-lasting protection for vehicles, pedestrians, and property. Available in a variety of sizes and finishes, they are suitable for warehouses, factories, car parks, and commercial sites.</p>
  <div class="page-no" style="left:444px;top:447px;">1</div>
</section>

<!-- Product -->
<section class="page" style="left:105px;top:612px;">
  <div class="photo" role="img" aria-label="Row of brushed steel bollards on a wet paved walkway" style="left:261px;top:0;width:212px;height:236px;background:linear-gradient(180deg,#9ea4a8 0%,#c7cbcd 45%,#e1e3e3 100%);"></div>
  <div class="photo" role="img" aria-label="Close view of a single stainless steel bollard beside a road" style="left:261px;top:236px;width:212px;height:237px;background:linear-gradient(180deg,#b9bec1 0%,#8f9599 50%,#d3d5d4 100%);"></div>
  <div class="abs yellow" style="left:0;top:43px;width:348px;height:53px;"></div>
  <div class="abs yellow" style="left:0;top:96px;width:10px;height:377px;"></div>
  <div class="abs heading" style="left:45px;top:55px;font-size:21px;">Standard Steel Bollard</div>
  <div class="abs" style="left:45px;top:114px;width:200px;">
    <p class="body-copy" style="width:165px;">The Standard Steel Bollard provides robust impact resistance while maintaining a clean, professional look. Ideal for industrial and commercial sites, it offers a cost-effective way to protect assets and control traffic flow.</p>
    <p class="spec-title" style="margin-top:11px;">Specifications:</p>
    <ul class="spec-list" style="margin-top:1px;">
      <li>Size: 900mm height, 140mm diameter</li>
      <li>Material: Galvanised Steel</li>
      <li>Color: Powder-coated Yellow or Black</li>
      <li>Use: Vehicle protection, site safety</li>
    </ul>
    <p class="spec-title" style="margin-top:15px;">Variations:</p>
    <ul class="spec-list" style="margin-top:1px;">
      <li>Small – 600mm</li>
      <li>Medium – 900mm</li>
      <li>Large – 1200mm</li>
    </ul>
  </div>
  <div class="page-no" style="left:444px;top:446px;">2</div>
</section>

<!-- Contact -->
<section class="page" style="left:622px;top:612px;">
  <div class="abs black" style="left:0;top:0;width:262px;height:465px;"></div>
  <div class="photo" role="img" aria-label="Customer service representative wearing a headset" style="left:262px;top:0;width:211px;height:465px;background:linear-gradient(180deg,#e2e5e7 0%,#d3d6d8 50%,#eef0f1 100%);"></div>
  <div class="abs yellow" style="left:0;top:465px;width:473px;height:8px;"></div>
  <div class="brand" style="left:35px;top:35px;"><span class="brand-square"></span>ARDEN LIMITED</div>
  <div class="abs yellow" style="left:0;top:92px;width:348px;height:53px;"></div>
  <div class="abs heading" style="left:45px;top:103px;font-size:21px;">Contact Us</div>
  <p class="abs contact-copy" style="left:35px;top:174px;width:180px;">We are here to help you choose the right products for your business. Contact us for orders, pricing, or additional product information.</p>
  <ul class="abs contact-list" style="left:29px;top:277px;">
    <li><svg viewBox="0 0 24 24"><path fill="#f5dc63" d="M6.6 10.8a15.1 15.1 0 0 0 6.6 6.6l2.2-2.2a1 1 0 0 1 1-.25 11.4 11.4 0 0 0 3.6.57 1 1 0 0 1 1 1V20a1 1 0 0 1-1 1A17 17 0 0 1 3 4a1 1 0 0 1 1-1h3.5a1 1 0 0 1 1 1c0 1.25.2 2.45.57 3.57a1 1 0 0 1-.25 1z"/></svg>Phone: +64 9 555 0142</li>
    <li><svg viewBox="0 0 24 24"><rect x="2" y="5" width="20" height="14" fill="#f5dc63"/><path d="M2 5l10 8 10-8" fill="none" stroke="#0f0f0f" stroke-width="2"/></svg>Email: hello@arden.co.nz</li>
    <li><svg viewBox="0 0 24 24" fill="none" stroke="#f5dc63" stroke-width="2"><circle cx="12" cy="12" r="9"/><path d="M3 12h18M12 3c3 3 3 15 0 18M12 3c-3 3-3 15 0 18"/></svg>Website: www.arden.co.nz</li>
    <li><svg viewBox="0 0 24 24"><path fill="#f5dc63" d="M12 2a7 7 0 0 0-7 7c0 5 7 13 7 13s7-8 7-13a7 7 0 0 0-7-7zm0 9.5A2.5 2.5 0 1 1 12 6.5a2.5 2.5 0 0 1 0 5z"/></svg>Address: 48 Harbour Road, Auckland, NZ</li>
  </ul>
</section>

</body>
</html>
```